Brimvaxo.com protective pads need Ads to sell products

We manufacture protective pads for car doors and are looking for ads to bring customers to the site on Facebook, twitter and display advertising. We need ads that get the message over that damage caused when parked is expensive and frequent and our pads will protect your car from this type of damage. This is a new product that we are starting to sell

```html
<!DOCTYPE html>
<html lang="en">
<head>
<meta charset="utf-8">
<title>Brimvaxo.com – Page</title>
<link href="https://fonts.googleapis.com/css2?family=Roboto:wght@400;500;700&family=Roboto+Condensed:wght@400;700&display=swap" rel="stylesheet">
<style>
:root{
  --bar:#3b5998;
  --page:#e9ebee;
  --card:#ffffff;
  --line:#dddfe2;
  --ink:#1d2129;
  --muted:#90949c;
  --link:#365899;
  --blue:#4080ff;
  --tile:#4f86f0;
  --red:#d3131a;
  --green:#42b72a;
}
*{box-sizing:border-box;margin:0;padding:0}
html,body{width:900px;height:1200px;overflow:hidden}
body{background:var(--page);font-family:"Roboto",Arial,sans-serif;color:var(--ink);position:relative}
.abs{position:absolute}
.card{position:absolute;background:var(--card);border:1px solid var(--line);border-radius:2px}

/* top bar */
.topbar{position:absolute;left:0;top:0;width:900px;height:29px;background:var(--bar)}
.topbar .mark{position:absolute;left:99px;top:5px;width:18px;height:18px;background:#fff;border-radius:2px}
.topbar .search{position:absolute;left:122px;top:5px;width:296px;height:16px;background:#fff;border-radius:2px;font-size:10px;padding:2px 7px;color:var(--ink)}
.topbar .search svg{position:absolute;right:7px;top:3px}
.topbar .user{position:absolute;left:550px;top:5px;display:flex;align-items:center;gap:5px;color:#fff;font-size:9px;font-weight:700}
.avatar{display:inline-block;background:linear-gradient(#8a7a6e,#4e4039);border-radius:1px}
.topbar .home{position:absolute;left:624px;top:8px;color:#fff;font-size:9px;font-weight:700}
.topbar .icons{position:absolute;left:668px;top:7px;display:flex;gap:9px}

/* left column */
.profile{position:absolute;left:100px;top:38px;width:111px;height:111px;background:#fff;border:1px solid var(--line);padding:3px}
.profile .inner{width:100%;height:100%;border:1px solid #eee;display:flex;flex-direction:column;align-items:center;justify-content:center;gap:4px}
.brandname{font-family:"Roboto Condensed",Arial,sans-serif;font-weight:700;color:var(--red);letter-spacing:.5px}
.brand-dot{width:10px;height:10px;border-radius:50%;background:var(--red)}
.pagename{position:absolute;left:99px;top:159px;font-size:14px;color:var(--ink);display:flex;align-items:center;gap:6px}
.pagename .verify{width:13px;height:13px;border-radius:50%;background:var(--blue);display:flex;align-items:center;justify-content:center}
.nav{position:absolute;left:99px;top:219px;width:117px;list-style:none;font-size:10px;color:#4b4f56}
.nav li{height:21.4px;line-height:21.4px;padding-left:7px}
.nav li.active{background:#dfe1e5;border-left:2px solid var(--bar);font-weight:700;color:var(--ink)}
.create{position:absolute;left:104px;top:380px;width:66px;height:15px;background:var(--green);color:#fff;font-size:8px;font-weight:500;text-align:center;line-height:15px;border-radius:2px}

/* ad cover */
.ad{position:relative;width:552px;height:208px;overflow:hidden}
.ad .photo{position:absolute;inset:0;background:linear-gradient(100deg,#5a0d10 0%,#b01a1f 30%,#8e1417 52%,#9a9a9a 53%,#c8c8c8 75%,#b5b5b5 100%)}
.ad .band{position:absolute;left:0;top:174px;width:260px;height:20px;background:rgba(211,19,26,.85);color:#fff;font-family:"Roboto Condensed",Arial,sans-serif;font-weight:700;font-size:11px;line-height:20px;padding-left:70px}
.ad .logobox{position:absolute;left:382px;top:20px;width:150px;height:104px;border:2px solid var(--red);display:flex;align-items:center;justify-content:center;gap:6px}
.ad .logobox .brandname{font-size:22px}
.ad .claim{position:absolute;right:18px;top:132px;text-align:right;font-family:"Roboto Condensed",Arial,sans-serif;font-weight:700;color:#111;line-height:19px;font-size:11px}
.ad .claim b{font-size:16px}
.ad .claim .xl{font-size:19px}

.cover{position:absolute;left:222px;top:30px}
.actionbar{position:absolute;left:222px;top:238px;width:552px;height:34px;background:#fff;border:1px solid var(--line);border-top:0}
.btngroup{position:absolute;left:8px;top:8px;display:flex;border:1px solid #ccd0d5;border-radius:2px;background:#f6f7f9}
.btngroup span{font-size:8px;font-weight:700;color:#4b4f56;padding:4px 7px;border-right:1px solid #ccd0d5;display:flex;align-items:center;gap:3px}
.btngroup span:last-child{border-right:0}
.contact{position:absolute;left:344px;top:8px;width:199px;height:18px;background:var(--blue);color:#fff;font-size:9.5px;text-align:center;line-height:18px;border-radius:2px}

/* composer */
.composer{left:222px;top:282px;width:334px;height:70px}
.composer .tabs{height:22px;border-bottom:1px solid var(--line);background:#f6f7f9;display:flex;align-items:center;gap:6px;padding-left:12px;font-size:8px;color:#4b4f56}
.composer .tabs a{color:var(--link);text-decoration:none}
.composer .write{display:flex;align-items:center;gap:9px;padding:8px 9px;font-size:9px;color:var(--muted)}

/* posts */
.post{left:222px;width:334px}
.post .head{position:absolute;left:7px;top:9px;display:flex;gap:7px}
.post .head .thumb{width:26px;height:26px;border:1px solid var(--line);display:flex;align-items:center;justify-content:center}
.post .head .thumb .brandname{font-size:5px}
.post .meta{font-size:7px;color:#4b4f56}
.post .meta a{color:var(--link);font-size:9px;text-decoration:none}
.post .meta .blue{color:var(--link)}
.post .meta small{display:block;color:var(--muted);font-size:7.5px;margin-top:3px}
.post .chev{position:absolute;right:10px;top:14px}
.post .body{position:absolute;left:7px;font-size:8px;line-height:11px;color:var(--ink);width:320px}
.media{position:absolute;left:7px;width:321px;overflow:hidden}
.acts{position:absolute;left:7px;width:320px;height:24px;border-top:1px solid var(--line);display:flex;align-items:center;gap:24px;padding-left:4px;font-size:8px;color:#4b4f56}
.acts span{display:flex;align-items:center;gap:5px}
.acts .me{position:absolute;right:8px;top:6px;width:12px;height:12px}
.stats{position:absolute;left:0;width:332px;background:#f6f7f9;border-top:1px solid var(--line)}
.reacts{position:absolute;left:9px;display:flex;align-items:center;font-size:8px;color:var(--link)}
.reacts i{width:10px;height:10px;border-radius:50%;border:1px solid #fff;margin-right:-2px;display:inline-block}
.topc{position:absolute;right:8px;font-size:8px;color:var(--link)}
.cwrite{position:absolute;left:8px;display:flex;align-items:center;gap:6px}
.cwrite .field{width:290px;height:22px;background:#fff;border:1px solid var(--line);font-size:9px;color:var(--muted);padding:5px 9px;position:relative}
.cwrite .field .ic{position:absolute;right:8px;top:5px;display:flex;gap:8px}

.redbanner{position:absolute;left:0;top:0;width:321px;height:74px;background:var(--red);color:#fff;text-align:center;font-family:"Roboto Condensed",Arial,sans-serif;font-weight:700;font-size:15px;line-height:18.5px;padding-top:10px}
.carphoto{position:absolute;left:0;top:74px;width:321px;height:246px;background:linear-gradient(160deg,#8a8a8a 0%,#4a4a4a 35%,#2e2e2e 60%,#1c1c1c 100%)}
.carphoto .logobox{position:absolute;left:181px;top:128px;width:119px;height:82px;border:1.5px solid #fff;display:flex;align-items:center;justify-content:center;gap:5px}
.carphoto .logobox .brandname{color:#fff;font-size:17px}
.carphoto .logobox .brand-dot{background:#fff}
.carphoto .url{position:absolute;left:207px;top:222px;color:#fff;font-size:10px}

/* right column */
.side{left:566px;width:208px}
.side .title{font-size:7.5px;font-weight:500;color:#4b4f56;padding:9px 5px 0;display:flex;justify-content:space-between;align-items:center}
.grid{display:grid;grid-template-columns:repeat(3,64.5px);gap:4px;padding:6px 4px}
.grid i{height:59px;background:var(--tile)}
.video{position:relative;background:var(--tile)}
.video .foot{position:absolute;left:0;right:0;bottom:0;height:20px;background:linear-gradient(transparent,rgba(20,40,90,.55));display:flex;justify-content:flex-end;gap:10px;align-items:center;padding:0 8px;color:#fff;font-size:7.5px}
.video .foot span{display:flex;align-items:center;gap:2px}
</style>
</head>
<body>

<header class="topbar">
  <span class="mark"></span>
  <div class="search">PageDemo.net
    <svg width="9" height="9" viewBox="0 0 10 10"><circle cx="4" cy="4" r="3" fill="none" stroke="#4b4f56" stroke-width="1.2"/><line x1="6.3" y1="6.3" x2="9" y2="9" stroke="#4b4f56" stroke-width="1.2"/></svg>
  </div>
  <div class="user"><span class="avatar" role="img" aria-label="User avatar" style="width:14px;height:14px"></span>Alex Carter</div>
  <div class="home">Home</div>
  <div class="icons">
    <svg width="14" height="12" viewBox="0 0 14 12"><circle cx="5" cy="3" r="2.5" fill="#fff"/><path d="M0 11c0-3 2-5 5-5s5 2 5 5z" fill="#fff"/><circle cx="10.5" cy="4" r="2" fill="#dfe3ee"/><path d="M9 7c3 0 5 1.5 5 4h-3z" fill="#dfe3ee"/></svg>
    <svg width="14" height="12" viewBox="0 0 14 12"><rect x="0" y="1" width="10" height="7" fill="#fff"/><path d="M2 8v3l3-3z" fill="#fff"/><rect x="5" y="4" width="9" height="6" fill="#dfe3ee"/></svg>
    <svg width="13" height="13" viewBox="0 0 13 13"><circle cx="6.5" cy="6.5" r="6" fill="#fff"/><path d="M3 3c2 1 2 3 4 3s1 3 3 4" stroke="#3b5998" fill="none"/></svg>
    <svg width="24" height="12" viewBox="0 0 24 12" style="margin-left:18px"><rect x="0" y="3" width="10" height="7" fill="#dfe3ee"/><path d="M16 5l3 3 3-3z" fill="#dfe3ee"/></svg>
  </div>
</header>

<!-- left column -->
<div class="profile"><div class="inner"><span class="brand-dot"></span><span class="brandname" style="font-size:17px">Brimvaxo</span></div></div>
<div class="pagename">Brimvaxo.com <span class="verify"><svg width="8" height="8" viewBox="0 0 8 8"><path d="M1 4l2 2 4-4" stroke="#fff" stroke-width="1.4" fill="none"/></svg></span></div>
<ul class="nav">
  <li class="active">Home</li><li>Photos</li><li>Likes</li><li>About</li><li>Videos</li><li>Welcome</li><li>Posts</li>
</ul>
<div class="create">Create a Page</div>

<!-- cover ad -->
<div class="cover">
  <div class="ad">
    <div class="photo" role="img" aria-label="Red hatchback car parked beside a road, photographed from the front three-quarter view"></div>
    <div class="band">WWW.BRIMVAXO.COM</div>
    <div class="logobox"><span class="brand-dot"></span><span class="brandname">Brimvaxo</span></div>
    <div class="claim"><b>Damage caused</b> when parked is expensive<br>and frequent and <b>our pads will protect your car</b><br>from this <span class="xl">type of damage.</span></div>
  </div>
</div>
<div class="actionbar">
  <div class="btngroup">
    <span><svg width="8" height="8" viewBox="0 0 8 8"><path d="M0 3h2v5H0zM3 3l2-3c1 0 1 1 1 2H8v3l-1 3H3z" fill="#4b67a1"/></svg>Liked ▾</span>
    <span><svg width="8" height="8" viewBox="0 0 8 8"><ellipse cx="4" cy="3.5" rx="4" ry="3.3" fill="#90949c"/></svg>Message</span>
    <span>··· More ▾</span>
  </div>
  <div class="contact">Contact Us</div>
</div>

<!-- composer -->
<div class="card composer">
  <div class="tabs">
    <svg width="9" height="9" viewBox="0 0 9 9"><path d="M1 8l1-3 5-5 2 2-5 5z" fill="#4b67a1"/></svg>Status
    <svg width="10" height="8" viewBox="0 0 10 8" style="margin-left:4px"><rect width="10" height="8" fill="#90949c"/><circle cx="5" cy="4" r="2" fill="#fff"/></svg>
    <a>Photo / Video</a>
    <span class="avatar" role="img" aria-label="User avatar" style="width:10px;height:10px;margin-left:auto"></span>
    <span style="margin-right:8px">▾</span>
  </div>
  <div class="write"><span class="avatar" role="img" aria-label="User avatar" style="width:26px;height:26px"></span>Write something on this Page...</div>
</div>

<!-- post 1 -->
<div class="card post" style="top:362px;height:260px">
  <div class="head">
    <div class="thumb"><span class="brandname">Brimvaxo</span></div>
    <div class="meta"><a>www.routebay.com/page/</a> changed their <span class="blue">cover photo.</span><small>2 mins · ◍</small></div>
  </div>
  <svg class="chev" width="8" height="5" viewBox="0 0 8 5"><path d="M0 0l4 4 4-4" stroke="#90949c" fill="none"/></svg>
  <div class="media" style="top:45px;height:123px">
    <div style="transform:scale(.5815);transform-origin:0 0">
      <div class="ad">
        <div class="photo" role="img" aria-label="Red hatchback car parked beside a road"></div>
        <div class="band">WWW.BRIMVAXO.COM</div>
        <div class="logobox"><span class="brand-dot"></span><span class="brandname">Brimvaxo</span></div>
        <div class="claim"><b>Damage caused</b> when parked is expensive<br>and frequent and <b>our pads will protect your car</b><br>from this <span class="xl">type of damage.</span></div>
      </div>
    </div>
  </div>
  <div class="acts" style="top:177px">
    <span><svg width="9" height="9" viewBox="0 0 8 8"><path d="M0 3h2v5H0zM3 3l2-3c1 0 1 1 1 2H8v3l-1 3H3z" fill="#90949c"/></svg>Like</span>
    <span><svg width="9" height="8" viewBox="0 0 9 8"><path d="M0 0h9v6H3L1 8V6H0z" fill="#90949c"/></svg>Comment</span>
    <span><svg width="9" height="8" viewBox="0 0 9 8"><path d="M5 0l4 3.5L5 7V5C2 5 1 6 0 8 0 4 2 2 5 2z" fill="#90949c"/></svg>Share</span>
    <span class="avatar me" role="img" aria-label="User avatar"></span>
  </div>
  <div class="stats" style="top:201px;height:58px">
    <div class="reacts" style="top:8px"><i style="background:#4080ff"></i><i style="background:#f0284a"></i><i style="background:#f7b125"></i><span style="margin-left:8px">1.6M</span></div>
    <div class="topc" style="top:8px">Top Comments ▾</div>
    <div class="cwrite" style="top:29px"><span class="avatar" role="img" aria-label="User avatar" style="width:20px;height:20px"></span>
      <div class="field">Write a comment...<span class="ic"><svg width="10" height="8" viewBox="0 0 10 8"><rect y="1" width="10" height="7" fill="#bec2c9"/><circle cx="5" cy="4.5" r="2" fill="#fff"/></svg><svg width="9" height="9" viewBox="0 0 9 9"><circle cx="4.5" cy="4.5" r="4" fill="none" stroke="#bec2c9"/></svg></span></div>
    </div>
  </div>
</div>

<!-- post 2 -->
<div class="card post" style="top:634px;height:528px">
  <div class="head">
    <div class="thumb"><span class="brandname">Brimvaxo</span></div>
    <div class="meta"><a>www.routebay.com/page/</a> changed their <span class="blue">cover photo.</span><small>June 17 · ◍</small></div>
  </div>
  <svg class="chev" width="8" height="5" viewBox="0 0 8 5"><path d="M0 0l4 4 4-4" stroke="#90949c" fill="none"/></svg>
  <p class="body" style="top:47px">Lorem ipsum dolor sit amet timeti ergo sum Lorem ipsum dolor sit amet timeti dolor sit amet timeti imeti ergo sum imeti ergo sum</p>
  <div class="media" style="top:81px;height:320px">
    <div class="redbanner">Damage caused when parked is expensive<br>and frequent and our pads will protect your<br>car from this type of damage.</div>
    <div class="carphoto" role="img" aria-label="Black and white close-up of a car's side doors with a black protective door pad shown in the corner">
      <div class="logobox"><span class="brand-dot"></span><span class="brandname">Brimvaxo</span></div>
      <div class="url">www.brimvaxo.com</div>
    </div>
  </div>
  <div class="acts" style="top:410px">
    <span><svg width="9" height="9" viewBox="0 0 8 8"><path d="M0 3h2v5H0zM3 3l2-3c1 0 1 1 1 2H8v3l-1 3H3z" fill="#90949c"/></svg>Like</span>
    <span><svg width="9" height="8" viewBox="0 0 9 8"><path d="M0 0h9v6H3L1 8V6H0z" fill="#90949c"/></svg>Comment</span>
    <span><svg width="9" height="8" viewBox="0 0 9 8"><path d="M5 0l4 3.5L5 7V5C2 5 1 6 0 8 0 4 2 2 5 2z" fill="#90949c"/></svg>Share</span>
    <span class="avatar me" role="img" aria-label="User avatar"></span>
  </div>
  <div class="stats" style="top:434px;height:93px">
    <div class="reacts" style="top:8px"><i style="background:#4080ff"></i><i style="background:#f0284a"></i><i style="background:#f7b125"></i><span style="margin-left:8px">1.6M</span></div>
    <div class="topc" style="top:10px">Top Comments ▾</div>
    <div style="position:absolute;left:8px;right:8px;top:28px;border-top:1px solid var(--line)"></div>
    <div style="position:absolute;left:9px;top:38px;font-size:8px;color:var(--link)">11,397 shares</div>
    <div style="position:absolute;right:8px;top:38px;font-size:8px;color:var(--muted)">15K Comments</div>
    <div class="cwrite" style="top:63px"><span class="avatar" role="img" aria-label="User avatar" style="width:20px;height:20px"></span>
      <div class="field">Write a comment...<span class="ic"><svg width="10" height="8" viewBox="0 0 10 8"><rect y="1" width="10" height="7" fill="#bec2c9"/><circle cx="5" cy="4.5" r="2" fill="#fff"/></svg><svg width="9" height="9" viewBox="0 0 9 9"><circle cx="4.5" cy="4.5" r="4" fill="none" stroke="#bec2c9"/></svg></span></div>
    </div>
  </div>
</div>

<!-- right column -->
<div class="card side" style="top:282px;height:29px;font-size:9px;padding:9px 7px">Personal Website</div>
<div class="card side" style="top:318px;height:26px;font-size:9px;color:var(--muted);padding:7px 7px;display:flex;gap:8px;align-items:center">
  <svg width="9" height="9" viewBox="0 0 10 10"><circle cx="4" cy="4" r="3" fill="none" stroke="#90949c" stroke-width="1.2"/><line x1="6.3" y1="6.3" x2="9" y2="9" stroke="#90949c" stroke-width="1.2"/></svg>Search for Posts on the Page
</div>
<div class="card side" style="top:352px;height:66px">
  <div style="display:flex;gap:7px;padding:4px 7px;border-bottom:1px solid var(--line);height:34px">
    <span class="avatar" role="img" aria-label="Friend avatar" style="width:20px;height:24px"></span>
    <div style="font-size:8px">1,955.550 people like this<div style="color:var(--muted);margin-top:3px">Sam Carter and 20 other friends</div></div>
  </div>
  <div style="display:flex;gap:14px;align-items:center;padding:9px 10px;font-size:7.5px">
    <svg width="11" height="10" viewBox="0 0 11 10"><circle cx="4" cy="3" r="2.5" fill="#bec2c9"/><path d="M0 10c0-3 2-4 4-4s4 1 4 4z" fill="#bec2c9"/><path d="M9 1v4M7 3h4" stroke="#bec2c9"/></svg>Invite friends to like this Page
  </div>
</div>
<div class="card side" style="top:427px;height:93px">
  <div class="title">ABOUT <svg width="6" height="9" viewBox="0 0 6 9"><path d="M1 1l3.5 3.5L1 8" stroke="#4b4f56" stroke-width="1.3" fill="none"/></svg></div>
  <div style="position:absolute;left:8px;top:34px;display:flex;gap:5px;font-size:8px;line-height:11.5px;width:195px"><span style="flex:none;width:7px;height:7px;border-radius:50%;border:1px solid #bec2c9;margin-top:2px"></span>Lorem ipsum dolor sit amet timeti ergo sum Lorem ipsum dolor sit amet timeti dolor sit amet timeti imeti ergo sum imeti ergo sum</div>
  <div style="position:absolute;left:8px;top:75px;display:flex;gap:5px;font-size:7.5px;color:var(--link)"><span style="width:7px;height:7px;border-radius:50%;border:1px solid #bec2c9;margin-top:2px"></span>http://www.pagedemo.net/</div>
</div>
<div class="card side" style="top:529px;height:215px">
  <div class="title">PHOTOS <svg width="6" height="9" viewBox="0 0 6 9"><path d="M1 1l3.5 3.5L1 8" stroke="#4b4f56" stroke-width="1.3" fill="none"/></svg></div>
  <div class="grid"><i></i><i></i><i></i><i></i><i></i><i></i><i></i><i></i><i></i></div>
</div>
<div class="card side" style="top:754px;height:190px">
  <div class="title">VIDEOS <svg width="6" height="9" viewBox="0 0 6 9"><path d="M1 1l3.5 3.5L1 8" stroke="#4b4f56" stroke-width="1.3" fill="none"/></svg></div>
  <div class="video" style="position:absolute;left:4px;top:25px;width:200px;height:98px">
    <svg style="position:absolute;left:73px;top:22px" width="56" height="56" viewBox="0 0 56 56"><circle cx="28" cy="28" r="26" fill="none" stroke="#fff" stroke-width="2.5"/><path d="M23 18l15 10-15 10z" fill="#fff"/></svg>
    <div class="foot"><span>▲ 139K</span><span>■ 2.2K</span></div>
  </div>
  <div class="video" style="position:absolute;left:4px;top:128px;width:98px;height:58px"><div class="foot" style="justify-content:space-between"><span>▲ 139K</span><span>■ 2.2K</span></div></div>
  <div class="video" style="position:absolute;left:106px;top:128px;width:98px;height:58px"><div class="foot" style="justify-content:space-between"><span>▲ 139K</span><span>■ 2.2K</span></div></div>
</div>

</body>
</html>
```